Alborada Fondos Invest - 2018 Website

We are an investment platform based in Madrid, Spain, that focuses on buying companies to improve them operationally and ignite growth through modernization, digitalization and a real hands on approach in the management of those companies we buy. We want to become a serious player in the private equity and money management industry and start approaching more institutional investors (such as pension funds, large family offices, etc.) in the coming months for an intense fundraising campaign.

For such purpose, we need a professional website with an impeccable design and streamlined communication. While we do want to provide some details in terms of what we do, who we are, our investment strategy, etc. we also want to be as vague as possible so that we do not limit ourselves to the claims we do on the website in terms of kind of investments, sectors, industries, geographies, etc. that we work on. For now we raise capital on a deal by deal basis, although our goal is to raise a discretionary pool of capital that we would deploy over 3-5 years. We are now building our track record as a team with already 2 investments which are showing massive growth potential and for which we have been able to execute the investment thesis as planned so far.

We need a simple and clear website with an incredibly professional image to go on the above mentioned roadshow and meet institutional investors.

For reference, we believe the following investment funds have very nice websites:

1) Brezo Private Equity - http://brezoequity-example.com/
2) Valdemar Capital - http://www.valdemarcapital-example.es/
3) Tresaco Capital - https://www.tresacocapital-example.com/

Thank you in advance.
Tomás Ribera Salcedo

Target Market(s)

Potential professional investors - from High Net Worth individuals, to more institutional investors such as Family Offices, Investment Funds, Pension Funds, etc.

Contact Information for Business Card

Name
Title
Contact Details (only for Andrés Villar Oña and Tomás Ribera Salcedo)

Font styles to use
Sans Serif

Colors

Designer to choose colors to be used in the design.

```html
<!DOCTYPE html>
<html lang="en">
<head>
<meta charset="utf-8">
<title>Alborada Ventures</title>
<link href="https://fonts.googleapis.com/css2?family=Lato:wght@300;400;700&display=swap" rel="stylesheet">
<style>
:root{
  --gold:#7b5f22;
  --gold-band:#7a6127;
  --ink:#222;
  --muted:#555;
  --line:#cfcfcf;
  --dark:#1f232b;
  --white:#fff;
}
*{box-sizing:border-box;margin:0;padding:0}
html,body{width:1200px;height:3727px;overflow:hidden}
body{font-family:'Lato',sans-serif;color:var(--ink);background:var(--white);position:relative}
.abs{position:absolute}
/* header */
.site-header{position:absolute;left:0;top:0;width:1200px;height:95px;background:var(--white)}
.brand{position:absolute;left:100px;top:14px;display:flex;align-items:center;gap:14px}
.brand-mark{width:48px;height:48px;background:var(--dark);border-radius:50%}
.brand-name{font-size:34px;font-weight:300;letter-spacing:2px;color:var(--dark);line-height:1}
.top-contact{position:absolute;right:100px;top:12px;display:flex;align-items:center;gap:14px;font-size:14px;color:var(--ink)}
.top-contact svg{vertical-align:-2px;margin-right:6px}
.investor-btn{border:2px solid var(--gold);border-radius:22px;padding:8px 16px;font-size:12px;font-weight:700;color:var(--ink)}
.main-nav{position:absolute;right:100px;top:62px;display:flex;gap:24px;font-size:14px;font-weight:400;text-transform:uppercase}
/* hero */
.hero{position:absolute;left:0;top:95px;width:1200px;height:480px;background:linear-gradient(180deg,#8c8f98 0%,#6e6a6e 45%,#8a6d55 70%,#4a4646 100%);text-align:center;color:var(--white)}
.hero h1{position:absolute;left:0;right:0;top:115px;font-size:78px;font-weight:300;letter-spacing:2px}
.hero p{position:absolute;left:0;right:0;top:210px;font-size:29px;font-weight:300}
.hero .btn-outline{position:absolute;left:506px;top:277px;width:190px;height:56px;border:2px solid var(--white);border-radius:28px;line-height:52px;font-size:16px;font-weight:700;letter-spacing:1px}
.dots{position:absolute;left:0;right:0;top:425px;display:flex;justify-content:center;gap:4px}
.dots span{width:13px;height:13px;border-radius:50%;border:2px solid var(--white)}
.dots span.on{background:var(--white)}
/* welcome */
.welcome-box{position:absolute;left:100px;top:680px;width:660px;height:485px;border:1px solid #999}
.welcome-box h2{position:absolute;left:40px;top:38px;font-size:34px;font-weight:300;line-height:1.35;text-transform:uppercase}
.welcome-box p{position:absolute;left:40px;width:500px;font-size:14px;line-height:1.9;color:var(--muted)}
.btn-gold{position:absolute;width:130px;height:46px;background:var(--gold);color:var(--white);border-radius:23px;font-size:13px;font-weight:700;text-align:center;line-height:46px}
.welcome-photo{position:absolute;left:700px;top:705px;width:400px;height:438px;background:linear-gradient(180deg,#1d6fb8 0%,#3b8fd0 45%,#1b5e9e 80%,#134a80 100%)}
/* strategy */
.strategy{position:absolute;left:0;top:1275px;width:1200px;height:393px;background:linear-gradient(90deg,#3a342c 0%,#57493a 50%,#4a443f 100%);color:var(--white)}
.strategy h2{position:absolute;left:100px;top:42px;font-size:34px;font-weight:300;line-height:1.4;letter-spacing:1px}
.strategy p{position:absolute;left:100px;top:155px;width:460px;font-size:14px;line-height:1.9}
.strategy .btn-gold{left:100px;top:290px}
.stat{position:absolute;top:67px;width:170px;text-align:center}
.stat svg{display:block;margin:0 auto}
.stat .num{position:absolute;left:0;right:0;top:44px;font-size:42px;font-weight:700}
.stat .cap{margin-top:16px;font-size:14px;line-height:1.45}
/* values */
.section-title{position:absolute;left:0;width:1200px;text-align:center;font-size:34px;font-weight:300;text-transform:uppercase;letter-spacing:1px}
.section-lead{position:absolute;left:0;width:1200px;text-align:center;font-size:14px;line-height:1.9;color:var(--muted)}
.value-card{position:absolute;top:1918px;width:235px;height:242px;border:1px solid #aaa;text-align:center}
.value-card svg{margin-top:32px}
.value-card h3{margin-top:12px;font-size:18px;font-weight:400;text-transform:uppercase}
.value-card p{margin:14px auto 0;width:190px;font-size:14px;line-height:1.8;color:var(--muted)}
.arrow-btn{position:absolute;width:36px;height:36px;border-radius:50%;border:1.5px solid #777;display:flex;align-items:center;justify-content:center;background:var(--white)}
.arrow-btn.light{border-color:#ddd;background:transparent}
/* testimonials */
.testimonials{position:absolute;left:0;top:2260px;width:1200px;height:413px;background:var(--gold-band);color:var(--white)}
.testimonials .section-title{top:62px}
.quote{position:absolute;top:152px;width:300px}
.avatar{position:absolute;left:0;top:0;width:74px;height:74px;border-radius:50%;background:#c7b8a6;border:3px solid var(--white)}
.quote blockquote{margin-left:94px;font-size:11.5px;font-style:italic;line-height:1.75}
.quote .who{margin-left:94px;margin-top:22px;font-size:10px;font-weight:700;text-transform:uppercase}
.quote .role{margin-left:94px;font-size:9px;font-style:italic}
.stars{position:absolute;left:0;top:135px;font-size:20px;color:#e6c24a;letter-spacing:3px}
/* blog */
.post{position:absolute;top:2870px;width:480px;height:190px}
.post-img{position:absolute;left:0;top:0;width:222px;height:185px;border:4px solid #ddd}
.post h3{position:absolute;left:245px;top:0;width:245px;font-size:18px;font-weight:400;line-height:1.45}
.post .meta{position:absolute;left:245px;top:66px;font-size:12px;color:var(--muted)}
.post p{position:absolute;left:245px;top:102px;width:225px;font-size:13px;line-height:1.85;color:var(--muted)}
.rule{position:absolute;left:100px;top:3135px;width:1000px;height:1px;background:var(--line)}
.partner{position:absolute;top:3288px;width:188px;height:105px;border:2px solid #ccc;display:flex;align-items:center;justify-content:center}
.partner span{width:120px;height:40px;background:#bdbdbd;border-radius:4px}
/* footer */
.site-footer{position:absolute;left:0;top:3515px;width:1200px;height:212px;background:var(--dark);color:var(--white);text-align:center;font-size:14px}
.socials{position:absolute;left:0;right:0;top:-22px;display:flex;justify-content:center;gap:16px}
.socials span{width:46px;height:46px;border-radius:50%;background:var(--white);border:3px solid var(--dark)}
.site-footer .line1{position:absolute;left:0;right:0;top:72px}
.site-footer .line2{position:absolute;left:0;right:0;top:112px}
.site-footer .line3{position:absolute;left:0;right:0;top:148px}
</style>
</head>
<body>

<header class="site-header">
  <div class="brand"><span class="brand-mark"></span><span class="brand-name">ALBORADA</span></div>
  <div class="top-contact">
    <span><svg width="13" height="13" viewBox="0 0 24 24"><path fill="#7b5f22" d="M6.6 10.8a15 15 0 006.6 6.6l2.2-2.2a1 1 0 011-.25 11.4 11.4 0 003.6.6 1 1 0 011 1V20a1 1 0 01-1 1A17 17 0 013 4a1 1 0 011-1h3.5a1 1 0 011 1c0 1.25.2 2.45.6 3.6a1 1 0 01-.25 1z"/></svg>+34 91 000 12 34</span>
    <span>|</span>
    <span><svg width="14" height="11" viewBox="0 0 24 18"><path fill="#7b5f22" d="M0 0h24v18H0z"/><path fill="none" stroke="#fff" stroke-width="2" d="M1 1l11 9 11-9"/></svg>info@alboradaventures-example.com</span>
    <span class="investor-btn">INVESTOR ACCESS</span>
  </div>
  <nav class="main-nav">
    <span>Home</span><span>About us</span><span>Services</span><span>Businesses</span><span>Blog</span><span>Career</span><span>Contact us</span>
    <svg width="14" height="14" viewBox="0 0 24 24"><circle cx="10" cy="10" r="7" fill="none" stroke="#222" stroke-width="3"/><path d="M15 15l7 7" stroke="#222" stroke-width="3"/></svg>
  </nav>
</header>

<section class="hero" role="img" aria-label="Madrid skyline with business towers at dusk">
  <h1>ALBORADA VENTURES</h1>
  <p>We are an investment platform based in Madrid, Spain</p>
  <span class="btn-outline">GET A QUOTE</span>
  <div class="dots"><span class="on"></span><span></span><span></span><span></span></div>
</section>

<section class="welcome">
  <div class="welcome-box">
    <h2>Welcome to<br>Alborada Ventures</h2>
    <p style="top:150px">Alborada Fondos Invest is a unique investment platform focused on value creation through consolidation, digitalization and internationalization of large, fragmented and traditional sectors. We build platforms and ecosystems, and ignite organic and inorganic growth in plateauing industries</p>
    <p style="top:290px">We do so by applying a true hands-on approach and deep involvement in operations throughout the life of the investment, and by rigorously analysing the sectors we invest in.</p>
    <span class="btn-gold" style="left:40px;top:383px">READ MORE</span>
  </div>
  <div class="welcome-photo" role="img" aria-label="Sailboats racing on a deep blue sea"></div>
</section>

<section class="strategy" role="img" aria-label="Darkened photo of a hand working on documents at a desk">
  <h2>ALBORADA FONDOS<br>INVEST STRATEGY</h2>
  <p>We provide exit and continuity solutions focused on growth for family-owned businesses in Spain, which will need to transition to professional management, to go under consolidation to grow and compete globally and to expand their geographical horizons,...</p>
  <span class="btn-gold">READ MORE</span>
  <div class="stat" style="left:591px">
    <svg width="150" height="150" viewBox="0 0 150 150"><circle cx="75" cy="75" r="67" fill="none" stroke="rgba(255,255,255,.25)" stroke-width="3"/><path d="M75 8 A67 67 0 1 1 22.4 33.5" fill="none" stroke="#fff" stroke-width="4"/></svg>
    <span class="num">85%</span>
    <div class="cap">Of Spanish businesses<br>are categorized as<br>family-owned</div>
  </div>
  <div class="stat" style="left:767px">
    <svg width="150" height="150" viewBox="0 0 150 150"><circle cx="75" cy="75" r="67" fill="none" stroke="rgba(255,255,255,.25)" stroke-width="3"/><path d="M75 8 A67 67 0 1 1 11.3 54.3" fill="none" stroke="#fff" stroke-width="4"/></svg>
    <span class="num">70%</span>
    <div class="cap">Contribution to Spain's<br>GDP by family-owned<br>businesses</div>
  </div>
  <div class="stat" style="left:944px">
    <svg width="150" height="150" viewBox="0 0 150 150"><circle cx="75" cy="75" r="67" fill="none" stroke="rgba(255,255,255,.25)" stroke-width="3"/><path d="M75 8 A67 67 0 1 1 11.3 54.3" fill="none" stroke="#fff" stroke-width="4"/></svg>
    <span class="num">70%</span>
    <div class="cap">Of private employment<br>generated by family<br>businesses</div>
  </div>
</section>

<section class="values">
  <h2 class="section-title" style="top:1755px">Our Values</h2>
  <p class="section-lead" style="top:1822px">Alborada Fondos Invest and its founders, as well as its co-investors, have conducted business with<br>immaculate reputation for decades in different regions of the world.</p>
  <span class="arrow-btn" style="left:30px;top:2022px"><svg width="12" height="12" viewBox="0 0 12 12"><path d="M8 1L3 6l5 5" fill="none" stroke="#555" stroke-width="1.6"/></svg></span>
  <div class="value-card" style="left:100px">
    <svg width="40" height="40" viewBox="0 0 24 24"><path fill="#7b5f22" d="M2 10h4v12H2zM8 21V10l5-8c1.5 0 2.5 1 2 3l-1 4h7a2 2 0 012 2.3l-1.5 8A2 2 0 0119.5 21z"/></svg>
    <h3>Excellence</h3>
    <p>As such, they are extremely concerned about preserving the Group's reputation</p>
  </div>
  <div class="value-card" style="left:355px">
    <svg width="40" height="40" viewBox="0 0 24 24"><path fill="#7b5f22" d="M2 6h15V2l6 6-6 6v-4H2zM22 14H7v-4l-6 6 6 6v-4h15z"/></svg>
    <h3>Integrity</h3>
    <p>As such, they are extremely concerned about preserving the Group's reputation</p>
  </div>
  <div class="value-card" style="left:610px">
    <svg width="40" height="40" viewBox="0 0 24 24"><circle cx="9" cy="14" r="6" fill="none" stroke="#7b5f22" stroke-width="4" stroke-dasharray="3 2"/><circle cx="9" cy="14" r="2" fill="#7b5f22"/><circle cx="18" cy="6" r="4" fill="none" stroke="#7b5f22" stroke-width="3" stroke-dasharray="2 1.5"/></svg>
    <h3>High Performance</h3>
    <p>As such, they are extremely concerned about preserving the Group's reputation</p>
  </div>
  <div class="value-card" style="left:865px">
    <svg width="44" height="40" viewBox="0 0 26 24"><circle cx="13" cy="6" r="4" fill="#7b5f22"/><circle cx="5" cy="9" r="3" fill="#7b5f22"/><circle cx="21" cy="9" r="3" fill="#7b5f22"/><path fill="#7b5f22" d="M7 22a6 6 0 0112 0zM0 20a5 5 0 018-3.5V20zM26 20a5 5 0 00-8-3.5V20z"/></svg>
    <h3>Teamwork</h3>
    <p>As such, they are extremely concerned about preserving the Group's reputation</p>
  </div>
  <span class="arrow-btn" style="left:1132px;top:2022px"><svg width="12" height="12" viewBox="0 0 12 12"><path d="M4 1l5 5-5 5" fill="none" stroke="#555" stroke-width="1.6"/></svg></span>
</section>

<section class="testimonials">
  <h2 class="section-title">Testimonials</h2>
  <span class="arrow-btn light" style="left:30px;top:208px"><svg width="12" height="12" viewBox="0 0 12 12"><path d="M8 1L3 6l5 5" fill="none" stroke="#eee" stroke-width="1.6"/></svg></span>
  <div class="quote" style="left:100px">
    <span class="avatar" role="img" aria-label="Portrait photo of the client"></span>
    <blockquote>&ldquo; At vero eos et accusamus et iustodio dignissimos ducimus qui blanditiispraesent ium voluptatum deleniti atqu.</blockquote>
    <div class="who">Lucía Prado</div>
    <div class="role">Financial Services Professional</div>
    <div class="stars">★★★★☆</div>
  </div>
  <div class="quote" style="left:445px">
    <span class="avatar" role="img" aria-label="Portrait photo of the client"></span>
    <blockquote>&ldquo; At vero eos et accusamus et iustodio dignissimos ducimus qui blanditiispraesent ium voluptatum deleniti atqu.</blockquote>
    <div class="who">Marco Ellison</div>
    <div class="role">National Urban Fellow at the Houston</div>
    <div class="stars">★★★★★</div>
  </div>
  <div class="quote" style="left:790px">
    <span class="avatar" role="img" aria-label="Portrait photo of the client"></span>
    <blockquote>&ldquo; At vero eos et accusamus et iustodio dignissimos ducimus qui blanditiispraesent ium voluptatum deleniti atqu.</blockquote>
    <div class="who">Ana Merino</div>
    <div class="role">Creative Strategist | Entrepreneur &amp; Upcoming</div>
    <div class="stars">★★★★☆</div>
  </div>
  <span class="arrow-btn light" style="left:1132px;top:208px"><svg width="12" height="12" viewBox="0 0 12 12"><path d="M4 1l5 5-5 5" fill="none" stroke="#eee" stroke-width="1.6"/></svg></span>
</section>

<section class="blog">
  <h2 class="section-title" style="top:2777px">Latest Blog</h2>
  <article class="post" style="left:100px">
    <div class="post-img" role="img" aria-label="Hands reviewing financial charts on paper" style="background:linear-gradient(135deg,#2f5d8a,#9fb6c8 60%,#e5e7ea)"></div>
    <h3>At vero eos et accusamus et iusto odio dignissimos</h3>
    <div class="meta">▦ 17/08/2017 &nbsp;|&nbsp; ● John Doe</div>
    <p>Et harum quidem rerum facilis est et expedita distinctio libero tepore cum soluta nobis est...</p>
  </article>
  <article class="post" style="left:618px">
    <div class="post-img" role="img" aria-label="Hand pointing at charts on a tablet" style="background:linear-gradient(135deg,#4a3a30,#9c8a7a 55%,#d9d4cf)"></div>
    <h3>At vero eos et accusamus et iusto odio dignissimos</h3>
    <div class="meta">▦ 17/08/2017 &nbsp;|&nbsp; ● John Doe</div>
    <p>Et harum quidem rerum facilis est et expedita distinctio libero tepore cum soluta nobis est...</p>
  </article>
  <div class="rule"></div>
</section>

<section class="partners">
  <h2 class="section-title" style="top:3202px">Our Partners</h2>
  <div class="partner" style="left:100px"><span></span></div>
  <div class="partner" style="left:303px"><span></span></div>
  <div class="partner" style="left:506px"><span></span></div>
  <div class="partner" style="left:709px"><span></span></div>
  <div class="partner" style="left:912px"><span></span></div>
</section>

<footer class="site-footer">
  <div class="socials"><span></span><span></span><span></span><span></span></div>
  <div class="line1">⌖ C/ Ejemplo 12, bajo 28001 Madrid &nbsp; | &nbsp; ☏ +34 91 000 12 34 &nbsp; | &nbsp; ✉ info@alboradaventures-example.com</div>
  <div class="line2">Help &nbsp;|&nbsp; FAQ &nbsp;|&nbsp; Support &nbsp;|&nbsp; Sitemap &nbsp;|&nbsp; Terms Of Use &nbsp;|&nbsp; Privacy Statement</div>
  <div class="line3">Copyrights © 2018, Alborada Ventures. All rights reserved.</div>
</footer>

</body>
</html>
```